VERIDAX Need a luxury modern business card designed.

Need a luxury modern business card designed. refer to the uploaded files for the company name and logo in the zip file under source files. i will making my descion on monday. so please send in before then so if we need to edit we will have the time. we have a trade show coming up and im on a deadline for printer.

Target Market(s)

high end clients

Contact Information for Business Card

Company nAme and logo. Calvin Ostrow Co-Founder / Project Manager Office # 416-555-0193 Cell # 416-555-0147 VERIDAX.CA Calvin@veridax.ca

Font styles to use
Other font styles liked:
• Modern

Requirements
Must have
• Company name and logo, contact info, using the black, gold and white color scheme.

```html
<!DOCTYPE html>
<html lang="en">
<head>
<meta charset="utf-8">
<title>VERIDAX Business Card</title>
<link rel="stylesheet" href="https://fonts.googleapis.com/css2?family=Montserrat:wght@300;400;500;700&display=swap">
<style>
  :root {
    --backdrop: #4e4e4e;
    --charcoal: #353233;
    --ink: #3a3738;
    --gold: #c2a84a;
    --olive-gold: #8c8150;
    --white: #ffffff;
    --rule-grey: #8a8a8a;
  }
  * { margin: 0; padding: 0; box-sizing: border-box; }
  html, body {
    width: 1200px; height: 1200px; overflow: hidden;
    background: var(--backdrop);
    font-family: "Montserrat", sans-serif;
  }
  .card {
    position: absolute; left: 220px; width: 760px; height: 456px;
  }
  .card-front {
    top: 95px;
    background: var(--charcoal);
    border-left: 5px solid var(--gold);
    border-bottom: 5px solid var(--gold);
  }
  .card-back { top: 649px; background: var(--white); }

  .wordmark {
    position: absolute; left: 0; width: 100%;
    text-align: center; font-weight: 300; line-height: 1;
  }
  .card-front .wordmark {
    top: 263px; font-size: 52px; letter-spacing: 18px;
    padding-left: 18px; color: var(--white);
  }
  .brand-rule { position: absolute; height: 1px; }
  .card-front .brand-rule.main { left: 206px; width: 337px; top: 314px; background: var(--white); }
  .tagline {
    position: absolute; display: flex; align-items: center; gap: 9px;
    font-weight: 700; line-height: 1; white-space: nowrap;
  }
  .tagline::before, .tagline::after {
    content: ""; display: block; height: 1px; flex: 1;
  }
  .card-front .tagline {
    left: 206px; width: 337px; top: 321px;
    font-size: 11px; letter-spacing: 5.6px; color: var(--white);
  }
  .card-front .tagline::before, .card-front .tagline::after { background: var(--white); }
  .website {
    position: absolute; left: 0; width: 100%; top: 401px;
    text-align: center; font-size: 14px; font-weight: 500;
    letter-spacing: 0.3px; color: var(--white);
  }

  .card-back .wordmark {
    left: 85px; width: 252px; top: 252px;
    font-size: 38px; letter-spacing: 12px; padding-left: 12px; color: var(--ink);
  }
  .card-back .brand-rule.main { left: 85px; width: 252px; top: 293px; background: var(--rule-grey); }
  .card-back .tagline {
    left: 85px; width: 252px; top: 299px;
    font-size: 9px; letter-spacing: 4px; color: #777;
    font-weight: 500;
  }
  .card-back .tagline::before, .card-back .tagline::after { background: var(--rule-grey); }

  .divider {
    position: absolute; left: 380px; top: 113px; width: 2px; height: 230px;
    background: #555;
  }
  .contact-block { position: absolute; left: 420px; top: 178px; color: var(--ink); }
  .person-name { font-size: 26px; font-weight: 700; letter-spacing: 0.5px; line-height: 1; }
  .person-title { margin-top: 7px; font-size: 16px; font-weight: 500; line-height: 1; }
  .contact-list { list-style: none; margin-top: 14px; }
  .contact-item {
    display: flex; align-items: center; height: 27px;
    font-size: 20px; font-weight: 700; line-height: 1;
  }
  .contact-item svg { width: 18px; height: 18px; margin-right: 11px; flex: none; }
  .address {
    position: absolute; left: 0; width: 100%; top: 383px;
    text-align: center; font-size: 16px; font-weight: 500; color: #222;
  }
</style>
</head>
<body>
  <section class="card card-front">
    <div class="wordmark">VERIDAX</div>
    <div class="brand-rule main"></div>
    <div class="tagline">LUXURY LANDSCAPES</div>
    <div class="website">WWW.VERIDAX.CA</div>
  </section>

  <section class="card card-back">
    <div class="wordmark">VERIDAX</div>
    <div class="brand-rule main"></div>
    <div class="tagline">LUXURY LANDSCAPES</div>

    <div class="divider"></div>

    <div class="contact-block">
      <div class="person-name">Calvin Ostrow</div>
      <div class="person-title">Project Manager</div>
      <ul class="contact-list">
        <li class="contact-item">
          <svg viewBox="0 0 18 18" aria-hidden="true"><rect x="4" y="1" width="10" height="16" rx="2" fill="none" stroke="var(--olive-gold)" stroke-width="1.8"/><circle cx="9" cy="14" r="1" fill="var(--olive-gold)"/></svg>
          416-555-0147
        </li>
        <li class="contact-item">
          <svg viewBox="0 0 18 18" aria-hidden="true"><path d="M3 2 L6 1.5 L8 6 L6 7.5 C7 10 8.5 11.5 10.5 12.5 L12 10.5 L16.5 12.5 L16 15.5 C9 16 2.5 9.5 3 2 Z" fill="var(--olive-gold)"/></svg>
          416-555-0193
        </li>
        <li class="contact-item">
          <svg viewBox="0 0 18 18" aria-hidden="true"><rect x="1" y="4" width="16" height="11" fill="none" stroke="var(--olive-gold)" stroke-width="1.6"/><path d="M1 4 L9 10.5 L17 4 M1 15 L7 9 M17 15 L11 9" fill="none" stroke="var(--olive-gold)" stroke-width="1.4"/></svg>
          Calvin@veridax.ca
        </li>
      </ul>
    </div>

    <div class="address">48 Alderwood Road Unit 7, Concord, ON L4K 2X9</div>
  </section>
</body>
</html>
```